Tidy Haven Path half fold brochure design

I need a brochure for a new company. The name of the company is Tidy Haven Path. I am a Professional Organizer. I am requesting a one fold brochure 11" wide x 8.5" high (obviously once folded 5.5" wide x 8.5" high) brochure. I have been told this may need to be designed as a flyer? I have attached a VERY BASIC layout of what I think I am looking for. I have also attached the original logos in all the different formats I have. I would like to have a very light green background & the text I have in orange please make orange. PLEASE feel free to add color to my "Tidy Haven Path" logo's and use light/soft green & orange shades if possible (OK to go darker for BOLD purposes) The brochure DOES NOT have to stick to this layout, again just what I THINK I want :) - THANK YOU

EDIT: 01-21-15 Remove MARLENE KUDSIK from all 3 places (front, bottom inside right & back) Remove just the KUDSIK from the 1st line on the back. PRIVACY & ETHICS on the back, please remove "PRIVACY &", leave Ethics and the 1st line of the text under it. Please remove all of the text following the 1st sentence. THANK YOU

Industry/Entity Type

It Company

```html
<!DOCTYPE html>
<html lang="en">
<head>
<meta charset="utf-8">
<title>Tidy Haven Path – Brochure Inside Spread</title>
<link href="https://fonts.googleapis.com/css2?family=Oswald:wght@400;500;600;700&family=Open+Sans:wght@300;400&display=swap" rel="stylesheet">
<style>
  :root {
    --orange: #df812e;
    --orange-deep: #d2742a;
    --peach: #f5d8bb;
    --sage: #eef1e2;
    --paper: #ffffff;
    --ink: #3a3a3a;
    --rule: #b9b0a6;
  }
  * { margin: 0; padding: 0; box-sizing: border-box; }
  html, body { width: 1200px; height: 927px; overflow: hidden; }
  body { font-family: "Open Sans", Arial, sans-serif; color: var(--ink); }
  .spread { position: relative; width: 1200px; height: 927px; overflow: hidden; }

  .panel { position: absolute; top: 0; height: 927px; width: 600px; }
  .panel--left { left: 0; background: var(--paper); }
  .panel--right { left: 600px; background: var(--sage); }

  .masthead { position: absolute; left: 0; top: 0; width: 600px; height: 80px; }
  .panel--left .masthead { background: var(--orange); }
  .panel--right .masthead { background: var(--peach); border-bottom: 1px solid #e9b58a; }

  .masthead__title {
    position: absolute; font-family: "Oswald", sans-serif; font-weight: 600;
    text-transform: uppercase; line-height: 1;
  }
  .panel--left .masthead__title { left: 32px; top: 26px; font-size: 50px; color: #fff; letter-spacing: 1px; }
  .panel--right .masthead__title { left: 97px; top: 26px; font-size: 52px; color: var(--orange); letter-spacing: 1px; }

  .intro {
    position: absolute; left: 36px; top: 88px; width: 560px;
    font-family: "Oswald", sans-serif; font-weight: 500; font-size: 17px;
    line-height: 22px; color: var(--orange-deep); text-transform: uppercase;
  }
  .intro-rule { position: absolute; left: 0; top: 142px; width: 600px; height: 3px; background: var(--orange); }

  .concern { position: absolute; left: 35px; width: 480px; }
  .concern__badge {
    position: absolute; left: 0; top: 0; width: 60px; height: 60px;
    border: 2px solid var(--orange); display: flex; align-items: center; justify-content: center;
  }
  .concern__badge span {
    width: 44px; height: 44px; background: var(--orange); color: #fff;
    font-family: "Open Sans", sans-serif; font-weight: 400; font-size: 20px;
    display: flex; align-items: center; justify-content: center;
  }
  .concern__title {
    position: absolute; left: 73px; top: 0; width: 405px; padding-bottom: 6px;
    border-bottom: 1px solid var(--rule);
    font-family: "Oswald", sans-serif; font-weight: 500; font-size: 20px; color: var(--orange);
  }
  .body-copy {
    font-size: 14.3px; line-height: 22.3px; text-align: justify; font-weight: 400; color: var(--ink);
  }
  .concern .body-copy { position: absolute; left: 73px; top: 44px; width: 405px; }

  .closing { position: absolute; left: 108px; top: 682px; width: 405px; }

  .definition { position: absolute; left: 94px; top: 128px; width: 406px; }
  .pitch { position: absolute; left: 94px; top: 269px; width: 406px; }

  .service { position: absolute; left: 94px; width: 420px; }
  .service__head {
    display: flex; align-items: center; gap: 8px;
    font-family: "Oswald", sans-serif; font-weight: 500; font-size: 15px;
    color: var(--orange); text-transform: uppercase;
  }
  .service__num {
    width: 16px; height: 16px; background: var(--orange); color: #fff; border: 1px solid var(--orange);
    outline: 1px solid #fff; outline-offset: -3px;
    font-size: 10px; font-weight: 600; display: flex; align-items: center; justify-content: center;
  }
  .service ul { list-style: none; margin-left: 54px; margin-top: 3px; }
  .service li { font-size: 14.5px; line-height: 22.5px; }
  .service li::before { content: "•"; color: var(--orange); margin-right: 3px; font-size: 11px; }

  .contact-strip {
    position: absolute; left: 0; top: 805px; width: 600px; height: 66px; background: var(--paper);
    border-top: 3px solid var(--orange);
  }
  .contact-strip p {
    position: absolute; left: 94px; top: 22px;
    font-family: "Oswald", sans-serif; font-weight: 500; font-size: 16.5px;
    color: var(--orange-deep); text-transform: uppercase;
  }

  .tagline-band { position: absolute; left: 0; top: 870px; width: 1200px; height: 57px; display: flex; }
  .tagline-band__half { width: 600px; height: 57px; }
  .tagline-band__half--left { background: var(--orange); border-top: 2px solid var(--orange); }
  .tagline-band__half--right { background: var(--peach); border-top: 2px solid #e9a36a; }
  .tagline {
    position: absolute; left: 82px; top: 14px; white-space: nowrap;
    font-family: "Oswald", sans-serif; font-weight: 600; font-size: 25px; letter-spacing: 8.1px;
    text-transform: uppercase; line-height: 1;
  }
  .tagline .light { color: #fff; }
  .tagline .warm { color: var(--orange); }
</style>
</head>
<body>
<main class="spread">

  <section class="panel panel--left">
    <header class="masthead"><h1 class="masthead__title">Getting Organized</h1></header>
    <p class="intro">Isn't all about everything being in its proper place.<br>It can also require overcoming fears and anxieties such as:</p>
    <div class="intro-rule"></div>

    <article class="concern" style="top:163px">
      <div class="concern__badge"><span>1</span></div>
      <h2 class="concern__title">“How do I start?”</h2>
      <p class="body-copy">You begin by getting help from a professional. No one can do everything; everyone needs a helping hand at times. (I bring my vehicle to a mechanic when it needs service, even for just a simple oil change!)</p>
    </article>

    <article class="concern" style="top:333px">
      <div class="concern__badge"><span>2</span></div>
      <h2 class="concern__title">“Am I going to have to get rid of ALL my things?”</h2>
      <p class="body-copy">Definitely not! There is a process that will help you decide what to keep and what you would be willing to part with. (I can help you determine the practical and monetary “worth” of something. Only you can determine its personal “value”.)</p>
    </article>

    <article class="concern" style="top:510px">
      <div class="concern__badge"><span>3</span></div>
      <h2 class="concern__title">“I don't have time”</h2>
      <p class="body-copy">Now you will! Getting organized will actually save you time. You will know where that “thing” is, find it quickly and avoid the time it takes to run out and purchase a new “thing”. (You will have actually created more time to enjoy the lifestyle that is important to you.)</p>
    </article>

    <p class="body-copy closing">We all have anxiety about something that prevents or inhibits us from taking action toward a solution. Whether you want someone to take over the project or a helping hand (nudge) is all you really need, a professional organizer is the perfect way to get started. Getting organized is going to be a process of progress, not perfection. It will require some level of support and continued work on you part, but the rewards will far outweigh the efforts.</p>
  </section>

  <section class="panel panel--right">
    <header class="masthead"><h1 class="masthead__title">What Is</h1></header>
    <p class="intro" style="left:98px">A Professional Organizer?</p>

    <p class="body-copy definition">“A Professional Organizer enhances the lives of clients by designing systems and processes using organizing principles and through transferring organizing skills. Professional Organizers help individuals and businesses take control of their surroundings, their time, their paper, and their systems for life.” – Guild of Home Organizing Professionals</p>

    <p class="body-copy pitch">Whether you are too busy, too confused, over whelmed, tired, stressed or just don't know where to start, I offer a variety of hands on services to help you bring a sense of fun, freedom and functionality to almost any space.</p>

    <div class="service" style="top:375px">
      <div class="service__head"><span class="service__num">1</span>Attic – to – Basement:</div>
      <ul><li>Sorting – Purging - Organizing</li></ul>
    </div>
    <div class="service" style="top:442px">
      <div class="service__head"><span class="service__num">2</span>Paper Control:</div>
      <ul><li>Sorting – Purging - Organizing</li><li>Household, home office &amp; home based filing systems</li></ul>
    </div>
    <div class="service" style="top:534px">
      <div class="service__head"><span class="service__num">3</span>Downsizing:</div>
      <ul><li>Sorting – purging - organizing - labeling</li><li>Packing &amp; unpacking</li></ul>
    </div>
    <div class="service" style="top:630px">
      <div class="service__head"><span class="service__num">4</span>Removal:</div>
      <ul><li>Light trash &amp; proper disposal</li><li>Donations &amp; light recyclables to proper locations</li><li>Shredding Service</li></ul>
    </div>
    <div class="service" style="top:743px">
      <div class="service__head"><span class="service__num">5</span>Follow Up:</div>
      <ul><li>Routine “clutter maintenance” visits</li></ul>
    </div>

    <div class="contact-strip"><p>For projects not listed above, please contact me.</p></div>
  </section>

  <footer class="tagline-band">
    <div class="tagline-band__half tagline-band__half--left"></div>
    <div class="tagline-band__half tagline-band__half--right"></div>
    <p class="tagline"><span class="light">Together we can conquer the </span><span class="warm">clutter and create clarity</span></p>
  </footer>

</main>
</body>
</html>
```